Law Firm Website

We are a small California based law firm specializing in business, corporate and litigation matters. We need to have our website redesigned. We are looking for a new and fresh look for our site, keeping in mind that we are a law firm.
What we don't want:
**the traditional "gavel" and "scales of justice" look
**anything too crazy
What we do want:
**sophisticated yet modern and fresh corporate look and feel
**samples of websites we really like:
http://www.tkrmllp.example
http://www.hollowaybrant.example/
we also like:
http://www.fentonardis.example/
http://www.qx.example/
http://www.moberly.example/
http://www.pvtr.example
http://www.npdlaw.example/
The content will be whatever is currently on our website (www.colterlawgroup.example). We will be selecting the winner based on originality and keeping the above requirements in mind. Please note that the photos that you use will be the ones that we will be using, so choose wisely because the photos will make a difference.
Target Market(s)
Corporate clients
Industry/Entity Type
Law Firm
Look and feel

```html
<!DOCTYPE html>
<html lang="en">
<head>
<meta charset="utf-8">
<title>Colter Law Group, LLP</title>
<link href="https://fonts.googleapis.com/css2?family=Roboto:wght@300;400;700&display=swap" rel="stylesheet">
<style>
:root{
  --sky:#dbe9f9;
  --band:#b3cfea;
  --paper:#f3f3f3;
  --navy:#1f5b93;
  --ink:#2b2b2b;
  --link:#1a77c6;
  --button:#0b74c9;
  --sage:#7eaa8c;
  --rule:#b8c9da;
  --white:#ffffff;
}
*{box-sizing:border-box;margin:0;padding:0}
html,body{width:1200px;height:991px;overflow:hidden}
body{position:relative;background:var(--paper);font-family:'Roboto',Arial,sans-serif;color:var(--ink)}
.backdrop{position:absolute;left:0;top:0;width:1200px;height:991px}
.site-header{position:absolute;left:120px;top:0;width:960px;height:106px;border-bottom:1px solid var(--rule)}
.brand{position:absolute;left:0;top:20px;display:flex;align-items:center;gap:10px}
.brand-mark{width:64px;height:64px;background:var(--button);border:3px solid var(--white)}
.brand-name{font-weight:700;font-size:24px;color:#2f4a66;line-height:26px;letter-spacing:.5px}
.brand-tag{font-weight:400;font-size:23px;color:#5b6f84;line-height:22px;letter-spacing:.5px}
.main-nav{position:absolute;right:10px;top:0;display:flex;height:105px}
.main-nav a{display:block;padding:60px 11px 0;font-size:16px;color:#333;text-decoration:none}
.main-nav a.active{background:var(--band);color:#111}
.sidebar{position:absolute;left:120px;width:300px}
.side-title{font-weight:300;font-size:24px;color:var(--navy);border-bottom:1px solid var(--navy);position:relative;padding-bottom:2px}
.side-title span{display:inline-block;border-bottom:3px solid var(--navy);margin-bottom:-3px;padding-right:2px}
.practice-list{list-style:none;margin-top:12px}
.practice-list li{height:26px;line-height:26px;font-size:13px;padding-left:22px;position:relative;color:var(--link)}
.practice-list li::before{content:"";position:absolute;left:8px;top:10px;width:6px;height:6px;background:var(--sage)}
.practice-list li.more::before{display:none}
.practice-list li.current{background:#eef4fb;color:#333}
.resource-item{font-size:13px;line-height:22px;padding:12px 0 10px}
.resource-item + .resource-item{border-top:1px dotted #888}
.resource-item.link{color:var(--link)}
.contact{font-size:13px;line-height:22px;margin-top:12px}
.contact a{color:var(--link);text-decoration:none}
.social{display:flex;gap:5px;margin-top:16px}
.social span{width:34px;height:34px;background:#9a9a9a;border-radius:3px}
.content{position:absolute;left:450px;top:145px;width:630px;height:782px;background:var(--white);box-shadow:0 1px 4px rgba(0,0,0,.35)}
.hero{position:relative;height:300px;border-bottom:5px solid var(--sage);box-sizing:content-box}
.hero-photo{position:absolute;inset:0;background:radial-gradient(ellipse at 70% 48%,#f6e7b0 0%,#c9902f 18%,#5a3a10 40%,#0c0906 68%,#000 100%)}
.hero-copy{position:absolute;left:20px;top:76px;color:var(--white)}
.hero-headline{font-weight:400;font-size:23px;line-height:24px}
.hero-headline em{font-style:normal;color:#3b97e3}
.hero-sub{font-weight:300;font-size:16px;line-height:24px;margin-top:10px}
.btn{display:inline-block;background:var(--button);color:var(--white);font-size:14px;padding:0 10px;height:30px;line-height:30px;text-decoration:none}
.btn.alt{background:var(--sage)}
.hero .btn{margin-top:18px}
.intro{position:absolute;left:19px;top:337px;width:595px;font-family:Arial,Helvetica,sans-serif;font-size:16px;line-height:30px;color:#333}
.card{position:absolute;top:481px;width:285px;height:251px;background:var(--paper);border-top:10px solid var(--sage);padding:14px 18px 0 20px}
.card h2{font-weight:300;font-size:24px;color:var(--navy);margin-bottom:14px}
.card p{font-size:13px;line-height:22px;color:#333}
.card .btn{margin-top:18px}
.news-item{font-size:13px;line-height:22px;color:var(--link);padding-bottom:10px}
.news-item + .news-item{border-top:1px dotted #888;padding-top:10px}
.site-footer{position:absolute;left:450px;top:947px;width:632px;font-size:12px;color:#333;display:flex;justify-content:space-between}
</style>
</head>
<body>
<svg class="backdrop" viewBox="0 0 1200 991" aria-hidden="true">
  <polygon points="0,0 1200,0 1200,208 0,588" fill="#dbe9f9"/>
  <polygon points="0,588 1200,208 1200,226 0,604" fill="#b3cfea"/>
</svg>

<header class="site-header">
  <div class="brand">
    <div class="brand-mark"></div>
    <div>
      <div class="brand-name">COLTER LAW GROUP, LLP</div>
      <div class="brand-tag">ATTORNEYS AT LAW</div>
    </div>
  </div>
  <nav class="main-nav">
    <a class="active" href="#">Home</a>
    <a href="#">About CLG</a>
    <a href="#">Practice Areas</a>
    <a href="#">Resources</a>
    <a href="#">Contact</a>
  </nav>
</header>

<aside class="sidebar" style="top:138px">
  <h2 class="side-title"><span>Our Practice Areas</span></h2>
  <ul class="practice-list">
    <li>Civil Litigation</li>
    <li>Employment Law</li>
    <li>Arbitration</li>
    <li>Mediation</li>
    <li class="current">Corporate Securities &amp; Corporate Governance</li>
    <li>Mergers &amp; Acquisitions</li>
    <li>Business &amp; Commercial Law Contracts</li>
    <li>Unlawful Detainers</li>
    <li>Products Liability</li>
    <li>Serious Personal Injury</li>
    <li>Investor and Consumer Protection</li>
    <li class="more">And many other matters</li>
  </ul>
</aside>

<aside class="sidebar" style="top:572px">
  <h2 class="side-title"><span>Resources</span></h2>
  <div class="resource-item link">Morbi ac leo congue, volutpat metus at.</div>
  <div class="resource-item">In molestie mauris et erat commodo, sit amet pharetra nunc pulvinar.</div>
</aside>

<aside class="sidebar" style="top:725px">
  <h2 class="side-title"><span>Contact Info</span></h2>
  <div class="contact">
    <strong>COSTA MESA OFFICE:</strong><br>
    4150 Harbor Vista Drive, 8th Floor Costa Mesa,<br>
    California 92626<br>
    <strong>Phone:</strong> (949) 555-0142 | <strong>Fax:</strong> (949) 555-0178<br>
    <strong>Email:</strong> <a href="#">info@colterlawgroup.example</a>
  </div>
  <div class="social"><span></span><span></span><span></span></div>
</aside>

<main class="content">
  <section class="hero">
    <div class="hero-photo" role="img" aria-label="Glowing golden key entering a bright keyhole on a dark background"></div>
    <div class="hero-copy">
      <h1 class="hero-headline"><em>THE KEY</em> TO <em>YOUR SUCCESS</em><br>IS HAVING THE RIGHT TEAM<br>SUPPORTING YOU.</h1>
      <p class="hero-sub">Our attorneys can provide a key component:<br>aggressive legal representation.</p>
      <a class="btn" href="#">Read More</a>
    </div>
  </section>
  <p class="intro"><strong>Colter Law Group, LLP</strong> provides quality legal representation to corporate as well as individual clients in the areas of business, corporate, securities, products liability, civil litigation (in State and Federal Courts), Alternative Dispute Resolution (arbitration and mediation), as well as a host of transactional matters.</p>
  <section class="card" style="left:20px">
    <h2>About CLG</h2>
    <p>Colter Law Group, LLP takes pride in providing quality legal representation to its clients, whether they are large corporations, partnerships, or individuals.</p>
    <a class="btn" href="#">Read More</a>
  </section>
  <section class="card" style="left:325px">
    <h2>Latest News</h2>
    <div class="news-item">Lorem ipsum dolor sit amet, consectetur adipiscing elit.</div>
    <div class="news-item">Fusce ac velit interdum, rutrum metus ut, faucibus enim.</div>
    <a class="btn alt" href="#" style="margin-top:6px">Read More</a>
  </section>
</main>

<footer class="site-footer">
  <span>© 2014 Colter Law Group, LLP | All rights reserved</span>
  <span>Terms of Use | Privacy Policy</span>
</footer>
</body>
</html>
```